Quillbox package design alternate designs & color themes

We want to see different options from multiple artists for our Brand Quillbox. We are an electronic accessories company that sell everything from camera accessories to mobile device accessories. We are looking for a simple yet professional design for our packaging. Attached is one example, however we are looking for your creativity. Please use any colors / design theme that you see fit for an electronics accessory company, that blend well with the current logo.

```html
<!DOCTYPE html>
<html lang="en">
<head>
<meta charset="utf-8">
<title>Quillbox Headphone Stand Packaging</title>
<link rel="stylesheet" href="https://fonts.googleapis.com/css2?family=Montserrat:wght@500;600;700&family=Poppins:wght@500;600;700&family=Open+Sans:wght@400;600&display=swap">
<style>
  :root {
    --bg: #f4f5f3;
    --panel: #ffffff;
    --panel-shade: #eeeeee;
    --green: #6ddc00;
    --green-dark: #5cc200;
    --ink: #111111;
    --line: #d9d9d9;
  }
  * { margin: 0; padding: 0; box-sizing: border-box; }
  html, body { width: 1200px; height: 1000px; overflow: hidden; background: var(--bg); }
  .canvas { position: relative; width: 1200px; height: 1000px; }

  .package { position: absolute; top: 40px; width: 410px; height: 920px; }
  .package--front { left: 120px; }
  .package--back { left: 670px; }

  .hang-tab {
    position: absolute; left: 0; top: 0; width: 360px; height: 140px;
    background: var(--panel); border: 1px solid var(--line); border-bottom: none;
  }
  .hang-slot { position: absolute; left: 125px; top: 50px; }

  .face {
    position: absolute; left: 0; top: 140px; width: 360px; height: 780px;
    background: linear-gradient(160deg, #ffffff 0%, #f7f7f7 60%, var(--panel-shade) 100%);
    border: 1px solid var(--line); overflow: hidden;
  }
  .side-strip {
    position: absolute; left: 360px; top: 140px; width: 50px; height: 780px;
    background: var(--green);
    display: flex; align-items: center; justify-content: center;
  }
  .side-strip__label {
    writing-mode: vertical-rl; transform: rotate(180deg);
    font-family: "Montserrat", sans-serif; font-weight: 600; font-size: 17px;
    letter-spacing: 3px; color: #ffffff;
  }

  .product-art {
    position: absolute; z-index: 0;
    background: linear-gradient(180deg, rgba(109,220,0,0.10), rgba(109,220,0,0.22));
    border-radius: 6px;
  }
  .package--front .product-art { left: 230px; top: 90px; width: 130px; height: 670px; }
  .package--back .product-art { left: 0; top: 90px; width: 50px; height: 630px; }

  .brand {
    position: absolute; z-index: 1; display: flex; align-items: center; gap: 10px;
    font-family: "Poppins", sans-serif; font-weight: 700; color: var(--ink);
  }
  .brand__dot { width: 16px; height: 16px; border-radius: 50%; background: var(--green); }
  .package--front .brand { left: 34px; top: 420px; font-size: 44px; }
  .package--back .brand { right: 30px; top: 80px; font-size: 40px; }

  .info { position: absolute; z-index: 1; right: 30px; text-align: right; color: var(--ink); }
  .title {
    top: 225px; font-family: "Montserrat", sans-serif; font-weight: 700;
    font-size: 23px; letter-spacing: 3px; color: var(--green);
  }
  .tagline { top: 270px; font-family: "Open Sans", sans-serif; font-size: 14px; line-height: 26px; }
  .colours { top: 410px; font-family: "Montserrat", sans-serif; }
  .colours__label { font-size: 11px; font-weight: 500; }
  .colours__option { display: flex; align-items: center; justify-content: flex-end; gap: 12px; font-size: 15px; font-weight: 700; margin-top: 6px; }
  .colours__option::before { content: ""; width: 9px; height: 9px; border: 1.5px solid var(--ink); border-radius: 50%; }
  .specs { top: 555px; font-family: "Montserrat", sans-serif; font-size: 11px; line-height: 14px; }
  .specs dt { font-weight: 500; margin-top: 12px; }
  .specs dt:first-child { margin-top: 0; }
  .specs dd { font-weight: 700; font-size: 12px; }
  .company { top: 690px; font-family: "Open Sans", sans-serif; font-size: 13px; line-height: 16px; color: var(--green-dark); font-style: normal; }
</style>
</head>
<body>
<main class="canvas">

  <section class="package package--front" aria-label="Front of package">
    <div class="hang-tab">
      <svg class="hang-slot" width="110" height="40" viewBox="0 0 110 40" aria-hidden="true">
        <path d="M18 12 H42 Q48 2 55 2 Q62 2 68 12 H92 Q106 12 106 24 Q106 36 92 36 H18 Q4 36 4 24 Q4 12 18 12 Z" fill="#f6f6f6" stroke="#c8c8c8" stroke-width="1.5"/>
      </svg>
    </div>
    <div class="face">
      <div class="product-art" role="img" aria-label="Outline drawing of the headphone stand in green"></div>
      <div class="brand"><span class="brand__dot"></span>Quillbox</div>
    </div>
    <div class="side-strip"><span class="side-strip__label">HEADPHONE STAND</span></div>
  </section>

  <section class="package package--back" aria-label="Back of package">
    <div class="hang-tab">
      <svg class="hang-slot" width="110" height="40" viewBox="0 0 110 40" aria-hidden="true">
        <path d="M18 12 H42 Q48 2 55 2 Q62 2 68 12 H92 Q106 12 106 24 Q106 36 92 36 H18 Q4 36 4 24 Q4 12 18 12 Z" fill="#f6f6f6" stroke="#c8c8c8" stroke-width="1.5"/>
      </svg>
    </div>
    <div class="face">
      <div class="product-art" role="img" aria-label="Partial outline drawing of the headphone stand in green"></div>
      <div class="brand"><span class="brand__dot"></span>Quillbox</div>
      <h1 class="info title">HEADPHONE STAND</h1>
      <p class="info tagline">High-Grade Lightweight Alumunium core<br>Stylishly designed to last</p>
      <div class="info colours">
        <p class="colours__label">Colour :</p>
        <p class="colours__option">Black</p>
        <p class="colours__option">White</p>
      </div>
      <dl class="info specs">
        <dt>Material :</dt><dd>High-Grade Alumunium</dd>
        <dt>Size :</dt><dd>95 x 95 x 220 mm</dd>
        <dt>Weight :</dt><dd>100 g</dd>
      </dl>
      <address class="info company">
        Quillbox<br>Electronic Accessories Company<br>Sample Address, Unit #00<br>City, 12345
      </address>
    </div>
    <div class="side-strip"><span class="side-strip__label">HEADPHONE STAND</span></div>
  </section>

</main>
</body>
</html>
```